"Keepers of the Lantern" - Book cover design

Background:
I have written a historical novel set in the Shanghai International Settlement in the 1920's and 1930's. My working title is 'Keepers of the Lantern'. The story is primarily set in Shanghai with a young Irishman as the main character. There is a back story set during the Irish War of Independence.

A Hollywood movie style pitch for this story might say
'Harbour Velvet' meets 'Tobias Renwick' or
'The Amber Duchess' meets 'The rain that bends the willow'

Here is the back cover promotional blurb I have written for the novel. Both the novel title and the cover design should simply, memorably and colourfully capture the vibe of this story:

"Logline - Love won and lost as civilisation dies

Shanghai 1927 – a city surrounded by warlord armies and run by gangsters. The wealthy international elite, sip cocktails in hotel bars, watching, amused, as armies wage war a street away. While they enjoy the cabarets, jazz clubs and taxi dances beneath lies a cesspool of vice, opium dens and fermenting revolution.

A young Irishman, Declan Hartigan, joins the Harbour Civic Constabulary (HCC), the transnational force protecting the Shanghai International Settlement. He carries the tragic memory of Niamh Ashcombe, the aristocratic girl he loved as a boy in Ireland, during the War of Independence. After Niamh's death - or presumed death, her body was never found - he gravitates to China, a place he and Niamh dreamed of visiting.

This haunted past confronts him anew when he unexpectedly meets his boyhood hero – Great War veteran Major Rory Penwick - who was present at Niamh’s apparent death. This reconnection ultimately leads to the truth of Niamh’s disappearance and Declan once more has love in his grasp.

Keepers of the Lantern is a sweeping story of corruption, revolution, war and love lost and found again, until tragedy has the final say. It unites the grand forces of history with the grand passion of two people’s forbidden love."

Target market:
Adult readers. age: 20+years
People who loves historical fiction, books about China, books set in the 1920s
People who buy novels on Bravolo

Task:
To create a cover for this novel. The cover needs to have the following information:
Title: "Keepers of the Lantern"
Author: "Colm Brannagh"

I would like to incorporate an imagery/icon that is representative of Shanghai in the 1920s (a city of jazz and opium, gangsters, spies, refugees, etc.) in the cover. I like the idea of using the silhouette of an opium pipe as well as silhouette of a man. Feel free to play with these two ideas and come up with different concepts.

Colour scheme:
Red, yellow, gold

Look and feel:
Modern, clean, simple, Art deco inspired design
Vibe of Shanghai in the 1920's - a city of jazz and opium, gangsters, spies, refugees, etc.
Simple typography, the title should not dominate the cover although it is helpful to have it recognizable from a distance

Note
This novel will be self e-published on Bravolo Readpad, Pagely, etc. The cover book design needs to look good as a small thumbnail on a computer screen, or smartphone or Tabro. The book cover should not be cluttered with text, or be too dark so that it makes an unattractive thumbnail on Bravolo or similar e-book sellers page. The full size cover should look good but when it shrinks down to thumbnail size it still looks good.

Attached with this brief are samples of novel covers that we would like you to use as inspiration. Please note how the icon/image dominates the cover while the text is still legible. I would like the cover of this novel to be different, unique and distinct when displayed with other similar books.

Shanghai in the 1920's and 1930's was an international city, controlled by various western powers. There was an international military presence, a multinational police force, many refugees from the Russian Revolution and later from Germany and Austria. It was a sophisticated city with 5-star hotels, fashionable nightclubs, jazz bands, a huge movie industry with many stars, gossip magazines, etc. It was a centre for cutting edge design, art and literature. So images that suggest a hip, between the wars Art Deco city would be more appropriate than say peasants working in rice fields. (Having said that, there was also great poverty in Shanghai, with street people and workers such as rickshaw pullers sharing the same space as movie stars and jazz musicians and gangster bosses).

Please check this link:
https://www.findquarry.example/search?q=images+of+1920%27s+shanghi&ie=utf-8&oe=utf-8&aq=t&rls=org.browsa:en-US:official&client=browsa-a

Target Market(s)

people who buy novels on Bravolo. People who love fiction, historical fiction, books about China, books set in the 1920's

Requirements
Must have

• A great book cover that is simple and eye catching and suitable for a computer screen thumbnail.
Should not have
• The book cover should not be cluttered with text, or be too dark so that it makes an unattractive thumbnail on Bravolo or similar ebook sellers page.
The full size cover should look good but when it shrinks down to thumbnail size it still looks good.

```html
<!DOCTYPE html>
<html lang="en">
<head>
<meta charset="utf-8">
<title>Keepers of the Lantern – Cover Spread</title>
<link rel="stylesheet" href="https://fonts.googleapis.com/css2?family=Arimo:wght@400;700&family=Oswald:wght@500;700&family=Rye&display=swap">
<style>
  :root {
    --stage: #dcd8cc;
    --back-olive: #343216;
    --spine-olive: #26240e;
    --panel-olive: #827d2b;
    --heading-yellow: #dccb5c;
    --body-cream: #ece8d2;
    --front-cream: #ebe6b4;
    --front-cream-light: #f1edc6;
    --author-olive: #857420;
    --title-red: #8b1c1c;
    --photo-dark: #4a4a1c;
    --photo-mid: #8f8c44;
    --photo-light: #c9c482;
  }
  * { box-sizing: border-box; margin: 0; padding: 0; }
  html, body { width: 1200px; height: 716px; overflow: hidden; }
  body { background: var(--stage); position: relative; }

  .cover-spread {
    position: absolute;
    left: 138px; top: 38px;
    width: 924px; height: 639px;
    display: flex;
  }

  /* Back cover */
  .back-cover {
    width: 447px; height: 100%;
    background: var(--back-olive);
    padding: 36px 12px 0 9px;
    color: var(--body-cream);
    font-family: "Arimo", Arial, sans-serif;
    font-size: 11.6px;
    line-height: 16.4px;
  }
  .back-heading {
    font-family: "Arimo", Arial, sans-serif;
    font-weight: 700;
    font-size: 16px;
    color: var(--heading-yellow);
    text-align: center;
    letter-spacing: 0.3px;
    margin-bottom: 8px;
  }
  .back-copy p { text-align: justify; }
  .back-copy .gap-large { margin-top: 30px; }
  .back-copy .gap-medium { margin-top: 16px; }
  .float-offset { float: right; width: 1px; height: 46px; }
  .blurb-panel {
    float: right; clear: right;
    width: 132px; height: 156px;
    margin: 0 13px 6px 14px;
    background: var(--panel-olive);
  }

  /* Spine */
  .spine {
    width: 24px; height: 100%;
    background: var(--spine-olive);
    display: flex; flex-direction: column;
    justify-content: space-between; align-items: center;
    padding: 30px 0 24px;
    font-family: "Oswald", Arial, sans-serif;
    font-weight: 700;
    font-size: 14px;
    letter-spacing: 0.6px;
    color: var(--heading-yellow);
  }
  .spine-text { writing-mode: vertical-rl; white-space: nowrap; }

  /* Front cover */
  .front-cover {
    position: relative;
    width: 453px; height: 100%;
    background: linear-gradient(180deg, var(--front-cream-light) 0%, var(--front-cream) 60%);
    overflow: hidden;
  }
  .front-author {
    position: absolute; right: 18px; top: 12px;
    font-family: "Oswald", Arial, sans-serif;
    font-weight: 700; font-size: 19px;
    letter-spacing: 0.5px;
    color: var(--author-olive);
  }
  .front-title {
    position: absolute; left: 40px; top: 66px; width: 400px;
    font-family: "Rye", Georgia, serif;
    font-weight: 400;
    color: var(--title-red);
    line-height: 1;
  }
  .front-title span { display: block; }
  .title-line-one { font-size: 50px; }
  .title-line-two { font-size: 28px; margin: 6px 0 0 64px; }
  .title-line-three { font-size: 56px; margin: -4px 0 0 96px; }

  .cover-photo {
    position: absolute; left: 0; bottom: 0;
    width: 100%; height: 288px;
    background:
      radial-gradient(ellipse at 52% 70%, var(--photo-dark) 0%, rgba(74,74,28,0.6) 32%, rgba(74,74,28,0) 60%),
      linear-gradient(180deg, rgba(235,230,180,0) 0%, var(--photo-light) 22%, var(--photo-mid) 60%, var(--photo-dark) 100%);
  }
</style>
</head>
<body>
  <main class="cover-spread">
    <section class="back-cover">
      <h2 class="back-heading">YOUR TITLE WILL COME HERE</h2>
      <div class="back-copy">
        <p>Lorem Ipsum is simply dummy text of the printing and typesetting industry. Lorem Ipsum has been the industry's standard dummy text ever since the 1500s, when an unknown printer took a galley of type and scrambled it to make a type specimen book. It has survived not only five centuries, but also the leap into electronic typesetting, remaining essentially unchanged. It was popularised in the 1960s with the release of Letterline sheets containing Lorem Ipsum passages, and more recently with desktop publishing software like Quillset PageForge including versions of Lorem Ipsum.</p>
        <div class="float-offset"></div>
        <div class="blurb-panel"></div>
        <p class="gap-large">It is a long established fact that a reader will be distracted by the readable content of a page when looking at its layout. The point of using Lorem Ipsum is that it has a more-or-less normal distribution of letters, as opposed to using 'Content here, content here', making it look like readable English.</p>
        <p class="gap-medium">Many desktop publishing packages and web page editors now use Lorem Ipsum as their default model text, and a search for 'lorem ipsum' will uncover many web sites still in their infancy. Various versions have evolved over the years, sometimes by accident, sometimes on purpose (injected humour and the like).</p>
      </div>
    </section>

    <aside class="spine">
      <span class="spine-text">KEEPERS OF THE LANTERN</span>
      <span class="spine-text">BY: COLM BRANNAGH</span>
    </aside>

    <section class="front-cover">
      <p class="front-author">BY: COLM BRANNAGH</p>
      <h1 class="front-title">
        <span class="title-line-one">KEEPERS</span>
        <span class="title-line-two">OF THE</span>
        <span class="title-line-three">LANTERN</span>
      </h1>
      <div class="cover-photo" role="img" aria-label="Sepia-toned photograph of an elderly man smoking a long opium pipe beside a woven screen and foliage"></div>
    </section>
  </main>
</body>
</html>
```